Bilingual school website redesign

The website oruvabilingualschool.example needs a new design

It is a private school from pre kinder to third grade

They teach Spanish and English

In the same website there is a section where teachers and parents interact
Updates

Reason: We are still waiting for approval from the school's teachers.

Target Market(s)

Mostly students' parents

Industry/Entity Type

Education

Number of Pages Required

3 page

Font styles to use
Sans Serif

Requirements
Must have
• Photo gallery
• Responsive design

```html
<!DOCTYPE html>
<html lang="en">
<head>
<meta charset="utf-8">
<title>Oruva School</title>
<link rel="stylesheet" href="https://fonts.googleapis.com/css2?family=Open+Sans:wght@300;400;600;700;800&display=swap">
<style>
:root{
  --blue:#2a8fe6;
  --blue-dark:#1f74c4;
  --yellow:#ffc400;
  --orange:#ff5a00;
  --pink:#ff2a8c;
  --green:#7ed321;
  --cyan:#16b1f0;
  --ink:#333;
  --muted:#666;
  --white:#fff;
}
*{box-sizing:border-box;margin:0;padding:0}
html,body{width:1200px;height:3240px;overflow:hidden}
body{font-family:"Open Sans",Arial,sans-serif;color:var(--ink);background:var(--white);position:relative}
.btn{display:inline-block;padding:10px 22px;border-radius:4px;color:var(--white);font-weight:700;font-size:15px;white-space:nowrap}
.btn-pink{background:var(--pink)}
.btn-orange{background:var(--orange)}
.btn-green{background:var(--green)}
.btn-blue{background:var(--blue)}
p{font-size:15px;line-height:1.6;color:var(--muted)}

/* header */
.site-header{position:absolute;top:0;left:0;width:1200px;height:52px;background:var(--blue);color:var(--white);z-index:3}
.brand{position:absolute;left:240px;top:13px;font-weight:800;font-size:20px;letter-spacing:1px;white-space:nowrap}
.header-contact{position:absolute;top:18px;font-size:12px;display:flex;align-items:center;gap:8px;white-space:nowrap}
.header-contact svg{width:13px;height:13px;flex:none}
.main-nav{position:absolute;top:52px;left:240px;display:flex;gap:6px;z-index:3}
.main-nav span{display:block;padding:12px 14px;font-size:13px;font-weight:700;color:var(--white);text-transform:uppercase;white-space:nowrap}
.main-nav span:first-child{color:var(--ink)}

/* hero */
.hero{position:absolute;top:52px;left:0;width:1200px;height:368px;background:linear-gradient(120deg,#b98a63,#e9b68c 45%,#7c6a55)}
.hero h1{position:absolute;left:240px;top:120px;color:var(--white);font-size:44px;font-weight:800;line-height:1.15;text-transform:uppercase}
.hero .down{position:absolute;left:240px;top:250px}

/* intro */
.intro{position:absolute;top:420px;left:0;width:1200px;height:320px}
.section-title{font-size:42px;font-weight:800;text-transform:uppercase;line-height:1.1;white-space:nowrap}
.intro .section-title{position:absolute;left:240px;top:30px}
.intro-text{position:absolute;left:240px;top:100px;width:440px}
.intro-text p+p{margin-top:12px}
.intro-photo{position:absolute;left:700px;top:100px;width:260px;height:200px;border-radius:6px;background:linear-gradient(135deg,#f2c08a,#e97a3a 60%,#6aa3d8)}

/* welcome */
.welcome{position:absolute;top:740px;left:0;width:1200px;height:310px;background:var(--yellow)}
.welcome h2{position:absolute;left:240px;top:40px;font-size:40px;font-weight:800;color:var(--ink)}
.welcome-text{position:absolute;left:240px;top:105px;width:400px}
.welcome-text p{color:#4a3a00}
.welcome .btn{position:absolute;left:240px;top:225px}
.quote-box{position:absolute;left:670px;top:40px;width:290px;height:230px;background:var(--orange);border-radius:6px;color:var(--white);padding:24px}
.quote-avatar{width:72px;height:72px;border-radius:50%;background:linear-gradient(135deg,#f5d0b0,#c2845a);border:3px solid var(--white)}
.quote-mark{position:absolute;left:112px;top:22px;font-size:56px;font-weight:800;line-height:1}
.quote-box p{margin-top:16px;color:var(--white);font-weight:700;font-style:italic;font-size:15px}

/* center */
.center{position:absolute;top:1050px;left:0;width:1200px;height:330px;background:linear-gradient(100deg,#e3d3c2,#cfae8d 50%,#8d6c52)}
.center h2{position:absolute;left:240px;top:95px;color:var(--white);font-size:40px;font-weight:300;line-height:1.15;text-transform:uppercase}
.center .btn{position:absolute;left:240px;top:205px;font-size:13px;display:flex;align-items:center;gap:8px}

/* programs */
.programs{position:absolute;top:1380px;left:0;width:1200px;height:400px}
.program{position:absolute;top:40px;width:340px}
.program .section-title{font-size:40px;margin-bottom:18px}
.program .btn{margin-top:26px}
.program-classes{left:240px}
.program-activities{left:610px}

/* news */
.news{position:absolute;top:1780px;left:0;width:1200px;height:460px;background:linear-gradient(120deg,#5a4a3c,#8a6a50 50%,#4a3b30)}
.news::after{content:"";position:absolute;inset:0;background:rgba(0,0,0,.35)}
.news h2{position:absolute;left:240px;top:45px;color:var(--white);font-size:40px;font-weight:800;z-index:1}
.news-arrows{position:absolute;left:915px;top:58px;display:flex;gap:4px;z-index:1}
.news-arrows span{width:18px;height:18px;background:var(--green);display:block}
.news-arrows span+span{background:var(--yellow)}
.news-cards{position:absolute;left:240px;top:148px;display:flex;gap:14px;z-index:1}
.news-card{width:230px;height:240px;background:var(--white);border-radius:4px;overflow:hidden}
.news-photo{height:170px}
.news-card h3{font-size:13px;font-weight:700;padding:10px 12px 4px;color:var(--ink);white-space:nowrap}
.news-card time{font-size:12px;color:#999;padding:0 12px;display:block}

/* gallery */
.gallery{position:absolute;top:2240px;left:0;width:1200px;height:610px}
.gallery .section-title{position:absolute;left:240px;top:40px;font-size:40px}
.gallery-grid{position:absolute;left:240px;top:120px;display:grid;grid-template-columns:repeat(3,230px);gap:12px 15px}
.gallery-photo{height:190px;border-radius:4px}
.gallery .btn{position:absolute;left:562px;top:536px;padding:8px 18px;font-size:13px}

/* contacts */
.contacts{position:absolute;top:2850px;left:0;width:1200px;height:390px;background:var(--orange);color:var(--white)}
.contacts h2{position:absolute;left:240px;top:55px;font-size:40px;font-weight:800}
.contact-list{position:absolute;left:240px;top:130px;list-style:none}
.contact-list li{display:flex;align-items:center;gap:14px;font-size:16px;margin-bottom:22px;white-space:nowrap}
.contact-list svg{width:22px;height:22px;flex:none}
.legal{position:absolute;left:240px;top:330px;font-size:12px;opacity:.85}
.map{position:absolute;left:610px;top:40px;width:350px;height:260px;background:linear-gradient(135deg,#eef1e6,#d9e2d0);border-radius:4px}
.map svg{position:absolute;left:151px;top:80px}
</style>
</head>
<body>

<header class="site-header">
  <div class="brand">ORUVA SCHOOL</div>
  <div class="header-contact" style="left:470px">
    <svg viewBox="0 0 24 24"><rect x="2" y="5" width="20" height="14" fill="none" stroke="#fff" stroke-width="2"/><path d="M2 5l10 8 10-8" fill="none" stroke="#fff" stroke-width="2"/></svg>
    info@oruvabilingualschool.example
  </div>
  <div class="header-contact" style="left:745px">
    <svg viewBox="0 0 24 24"><path d="M6 2l4 4-2 3c1 3 4 6 7 7l3-2 4 4-3 4C10 22 2 14 2 5z" fill="#fff"/></svg>
    (555) 010 2847
  </div>
</header>

<nav class="main-nav">
  <span style="background:var(--yellow)">Home</span>
  <span style="background:var(--green)">Our School</span>
  <span style="background:var(--pink)">Classes</span>
  <span style="background:var(--green)">Activities</span>
  <span style="background:var(--pink)">Gallery</span>
  <span style="background:var(--orange)">Contacts</span>
</nav>

<section class="hero" role="img" aria-label="Photo of young children smiling in a classroom">
  <h1>Excepteur sint<br>occaecat talent</h1>
  <svg class="down" width="40" height="40" viewBox="0 0 40 40"><circle cx="20" cy="20" r="18" fill="none" stroke="#fff" stroke-width="2"/><path d="M20 11v17M13 21l7 7 7-7" fill="none" stroke="#fff" stroke-width="2.5"/></svg>
</section>

<section class="intro">
  <h2 class="section-title"><span style="color:var(--pink)">School</span> <span style="color:var(--yellow)">for</span> <span style="color:var(--cyan)">young</span> <span style="color:var(--green)">Picassos</span></h2>
  <div class="intro-text">
    <p>Our classrooms welcome children from pre kinder to third grade, learning every day in Spanish and English. Small groups and caring teachers help each child grow with confidence and joy.</p>
    <p>Art, music and play are part of every lesson, so young minds discover languages naturally. Parents follow progress closely with teachers.</p>
  </div>
  <div class="intro-photo" role="img" aria-label="Photo of children reading and drawing together"></div>
</section>

<section class="welcome">
  <h2>WELCOME!</h2>
  <div class="welcome-text">
    <p>We are a private bilingual school where learning feels like an adventure. Our team guides every child with patience and warmth, building strong habits for reading, thinking and friendship in two languages.</p>
  </div>
  <span class="btn btn-pink">Read More</span>
  <div class="quote-box">
    <div class="quote-avatar" role="img" aria-label="Portrait photo of a teacher"></div>
    <div class="quote-mark">&ldquo;</div>
    <p>Every child is an artist and a learner. We help them discover both voices.</p>
  </div>
</section>

<section class="center" role="img" aria-label="Photo of a child drawing with colored pencils">
  <h2>Children's<br>Center</h2>
  <span class="btn btn-blue">
    <svg width="16" height="16" viewBox="0 0 24 24"><circle cx="12" cy="12" r="10" fill="none" stroke="#fff" stroke-width="2"/><path d="M2 12h20M12 2c4 4 4 16 0 20M12 2c-4 4-4 16 0 20" fill="none" stroke="#fff" stroke-width="2"/></svg>
    Children's Web Center
  </span>
</section>

<section class="programs">
  <div class="program program-classes">
    <h2 class="section-title"><span style="color:var(--cyan)">Children's</span><br><span style="color:var(--yellow)">Classes</span></h2>
    <p>Small bilingual classes follow a gentle daily rhythm of reading, numbers, science and stories. Teachers adapt each activity to the age and pace of the group, keeping learning playful and clear.</p>
    <span class="btn btn-orange">Read More</span>
  </div>
  <div class="program program-activities">
    <h2 class="section-title"><span style="color:var(--pink)">Special</span><br><span style="color:var(--green)">Activities</span></h2>
    <p>Painting, dance, music, sports and garden days fill the week with new skills. Special events invite families to join, celebrate and see the talents of their children shine.</p>
    <span class="btn btn-green">Read More</span>
  </div>
</section>

<section class="news">
  <h2>LATEST NEWS</h2>
  <div class="news-arrows"><span></span><span></span></div>
  <div class="news-cards">
    <article class="news-card">
      <div class="news-photo" role="img" aria-label="Photo of a smiling girl at her desk" style="background:linear-gradient(135deg,#f3c98f,#e08a4a)"></div>
      <h3>Spring art fair opens to families</h3>
      <time>March 12, 2024</time>
    </article>
    <article class="news-card">
      <div class="news-photo" role="img" aria-label="Photo of pupils working together in class" style="background:linear-gradient(135deg,#9cc6e8,#e7b37c)"></div>
      <h3>New reading corner in Spanish</h3>
      <time>March 05, 2024</time>
    </article>
    <article class="news-card">
      <div class="news-photo" role="img" aria-label="Photo of children raising their hands" style="background:linear-gradient(135deg,#f2d6a2,#d47c5a)"></div>
      <h3>Parents meeting on Friday</h3>
      <time>February 27, 2024</time>
    </article>
  </div>
</section>

<section class="gallery">
  <h2 class="section-title"><span style="color:var(--blue)">Last</span> <span style="color:var(--orange)">added</span> <span style="color:var(--green)">photos</span></h2>
  <div class="gallery-grid">
    <div class="gallery-photo" role="img" aria-label="Photo of a boy studying" style="background:linear-gradient(135deg,#a9cbe6,#e6b88a)"></div>
    <div class="gallery-photo" role="img" aria-label="Photo of children painting" style="background:linear-gradient(135deg,#c98a9e,#6e5b8a)"></div>
    <div class="gallery-photo" role="img" aria-label="Photo of a girl with letter blocks" style="background:linear-gradient(135deg,#e7c08c,#b86e4a)"></div>
    <div class="gallery-photo" role="img" aria-label="Photo of a teacher with pupils" style="background:linear-gradient(135deg,#e9e4dc,#b7a592)"></div>
    <div class="gallery-photo" role="img" aria-label="Photo of a chalkboard with letters" style="background:linear-gradient(135deg,#5f7a5a,#3e5040)"></div>
    <div class="gallery-photo" role="img" aria-label="Photo of children playing with toys" style="background:linear-gradient(135deg,#f0b36a,#8fb7d8)"></div>
  </div>
  <span class="btn btn-blue">View All</span>
</section>

<footer class="contacts">
  <h2>CONTACTS</h2>
  <ul class="contact-list">
    <li><svg viewBox="0 0 24 24"><path d="M6 2l4 4-2 3c1 3 4 6 7 7l3-2 4 4-3 4C10 22 2 14 2 5z" fill="#fff"/></svg>(555) 010 2847</li>
    <li><svg viewBox="0 0 24 24"><path d="M12 2a7 7 0 0 0-7 7c0 5 7 13 7 13s7-8 7-13a7 7 0 0 0-7-7z" fill="#fff"/><circle cx="12" cy="9" r="2.5" fill="#ff5a00"/></svg>48 Avenida del Sol, Barrio Centro</li>
    <li><svg viewBox="0 0 24 24"><rect x="2" y="5" width="20" height="14" fill="none" stroke="#fff" stroke-width="2"/><path d="M2 5l10 8 10-8" fill="none" stroke="#fff" stroke-width="2"/></svg>info@oruvabilingualschool.example</li>
  </ul>
  <div class="legal">&copy; 2024 Oruva School. All rights reserved. Privacy Policy</div>
  <div class="map" role="img" aria-label="Street map showing the school location">
    <svg width="48" height="64" viewBox="0 0 48 64"><path d="M24 2A22 22 0 0 0 2 24c0 16 22 38 22 38s22-22 22-38A22 22 0 0 0 24 2z" fill="#ff2a8c"/><circle cx="24" cy="24" r="8" fill="#fff"/></svg>
  </div>
</footer>

</body>
</html>
```